My Insurance Agency Show Display

I need to design a 10 ft x 8 ft backdrop for a show display. This is a pop up fabric most likely display that will be used for a show booth. I need someone to design something more attractive with my logo and make it more flashy so people can see and remember my company. I have attached my rough design so far. I would like it to look more modern. The photo in the design does not have to be used.

This is for an insurance agency that provides Home, Auto, Life and Health products to consumers. We also provide Renters insurance, Commercial, RV, mobile homes, and other products to our customers.

Target Market(s)

Home Owners, and Multiple Auto Owners

Industry/Entity Type

Property and Causality Insurance

Font styles to use
Sans Serif

Colors
0054AA
0677BA
7BADD7
CADEEF
E8F1F8
00AB8E
00BBA5
67D7C9
C6EFE9
E9F9F6

Requirements
Must have
• Attractive Modern Layout
Nice to have
• new and creative. Something that pops with color
Should not have
• Any affiliation to other insurance agencies.

```html
<!DOCTYPE html>
<html lang="en">
<head>
<meta charset="UTF-8">
<title>Keystone Insurance Agency – Show Backdrop</title>
<link href="https://fonts.googleapis.com/css2?family=Poppins:wght@400;500;600;700&display=swap" rel="stylesheet">
<style>
  :root {
    --pink: #d81b60;
    --pink-dark: #c4174f;
    --blue: #46a8dc;
    --ink: #1f1f22;
    --white: #ffffff;
    --stage: #d2d2d2;
  }
  * { margin: 0; padding: 0; box-sizing: border-box; }
  html, body { width: 842px; height: 1200px; overflow: hidden; }
  body { background: var(--stage); font-family: "Poppins", sans-serif; color: var(--ink); }

  .backdrop {
    position: absolute; left: 0; top: 263px;
    width: 842px; height: 674px; overflow: hidden;
    background: var(--white);
    box-shadow: 0 10px 24px rgba(0,0,0,.18);
  }
  .backdrop-shapes { position: absolute; inset: 0; width: 842px; height: 674px; }

  .phone {
    position: absolute; left: 28px; top: 20px;
    display: flex; align-items: center; gap: 6px;
    font-size: 29px; font-weight: 600; letter-spacing: -0.5px; color: var(--ink);
  }
  .phone svg { width: 22px; height: 22px; }

  .brand {
    position: absolute; left: 293px; top: 22px; width: 254px;
    display: flex; flex-direction: column; align-items: center;
    color: var(--white); font-weight: 700; text-align: center;
  }
  .brand-mark { width: 34px; height: 34px; border: 3px solid var(--white); margin-bottom: 14px; }
  .brand-name { font-size: 20px; line-height: 1.2; letter-spacing: 0.5px; }
  .brand-sub { font-size: 15px; letter-spacing: 5px; margin-top: 2px; }

  .headline {
    position: absolute; left: 0; top: 340px; width: 842px;
    text-align: center; font-size: 44px; line-height: 45px; font-weight: 400;
    text-transform: uppercase; letter-spacing: -0.5px;
  }
  .headline strong { color: var(--pink); font-weight: 700; }

  .intro {
    position: absolute; left: 80px; top: 440px; width: 682px;
    text-align: center; font-size: 11.4px; line-height: 18px; color: var(--ink);
  }

  .services { position: absolute; left: 0; top: 512px; width: 842px; height: 100px; }
  .service {
    position: absolute; top: 0; width: 100px; margin-left: -50px;
    display: flex; flex-direction: column; align-items: center;
  }
  .service svg { width: 72px; height: 72px; }
  .service-label { margin-top: 6px; font-size: 14.5px; font-weight: 500; text-transform: uppercase; color: var(--ink); }

  .contact-band {
    position: absolute; left: 0; bottom: 0; width: 842px; height: 44px;
    background: var(--pink);
    display: flex; align-items: center; color: var(--white); font-size: 15px; font-weight: 500;
  }
  .contact-item { position: absolute; display: flex; align-items: center; gap: 8px; }
  .contact-item svg { width: 18px; height: 18px; }
  .contact-address { left: 92px; }
  .contact-email { left: 480px; }
</style>
</head>
<body>
<main class="backdrop">
  <svg class="backdrop-shapes" viewBox="0 0 1077 862" preserveAspectRatio="none">
    <defs>
      <linearGradient id="familyTones" x1="0" y1="0" x2="1" y2="1">
        <stop offset="0" stop-color="#e9eef2"/>
        <stop offset="0.45" stop-color="#c99a82"/>
        <stop offset="0.75" stop-color="#5a86b8"/>
        <stop offset="1" stop-color="#2d3138"/>
      </linearGradient>
      <linearGradient id="doctorTones" x1="0" y1="0" x2="0.6" y2="1">
        <stop offset="0" stop-color="#f1f2f4"/>
        <stop offset="0.5" stop-color="#dfe2e6"/>
        <stop offset="0.8" stop-color="#d8b48a"/>
        <stop offset="1" stop-color="#c9ccd2"/>
      </linearGradient>
    </defs>
    <rect class="photo-family" x="0" y="0" width="560" height="600" fill="url(#familyTones)" role="img" aria-label="Photo of a smiling family of four"/>
    <rect class="photo-doctor" x="560" y="0" width="517" height="600" fill="url(#doctorTones)" role="img" aria-label="Photo of a doctor's hands forming a roof over a small wooden house and paper family figures"/>
    <rect x="0" y="0" width="370" height="135" fill="#ffffff" opacity="0.85"/>
    <polygon class="brand-panel" points="375,0 700,0 700,150 538,250 375,150" fill="var(--pink)"/>
    <polygon class="content-field" points="0,560 538,262 1077,560 1077,862 0,862" fill="#ffffff"/>
    <polyline class="accent-line" points="0,574 538,278 1077,574" fill="none" stroke="var(--blue)" stroke-width="4"/>
    <polygon class="accent-diamond" points="455,342 538,298 620,342 538,386" fill="var(--blue)"/>
  </svg>

  <div class="phone">
    <svg viewBox="0 0 24 24" fill="none" stroke="#46a8dc" stroke-width="2.4" stroke-linecap="round"><path d="M5 3h4l2 5-2.5 1.5a11 11 0 0 0 6 6L16 13l5 2v4a2 2 0 0 1-2 2A16 16 0 0 1 3 5a2 2 0 0 1 2-2z"/><path d="M15 3a6 6 0 0 1 6 6M15 7a2 2 0 0 1 2 2"/></svg>
    <span>555-208-0148</span>
  </div>

  <div class="brand">
    <div class="brand-mark"></div>
    <div class="brand-name">KEYSTONE INSURANCE</div>
    <div class="brand-sub">AGENCY</div>
  </div>

  <h1 class="headline"><strong>Protecting</strong> What<br>Matters Most To <strong>You</strong></h1>

  <p class="intro">Our comprehensive insurance services provide you with peace of mind, ensuring that your assets, health, and loved ones are safeguarded against unforeseen circumstances. Trust in our expertise to navigate the complexities of insurance and secure a brighter future for you and your family.</p>

  <section class="services">
    <div class="service" style="left:138px">
      <svg viewBox="-36 -36 72 72"><polygon points="0,-34 29.4,-17 29.4,17 0,34 -29.4,17 -29.4,-17" fill="#fff" stroke="#d81b60" stroke-width="2"/><polygon points="0,-29 25.1,-14.5 25.1,14.5 0,29 -25.1,14.5 -25.1,-14.5" fill="#46a8dc"/><path d="M-14 1 L0 -12 L14 1 L11 1 L11 13 L3 13 L3 5 L-3 5 L-3 13 L-11 13 L-11 1 Z" fill="#fff"/></svg>
      <span class="service-label">Home</span>
    </div>
    <div class="service" style="left:233px">
      <svg viewBox="-36 -36 72 72"><polygon points="0,-34 29.4,-17 29.4,17 0,34 -29.4,17 -29.4,-17" fill="#fff" stroke="#d81b60" stroke-width="2"/><polygon points="0,-29 25.1,-14.5 25.1,14.5 0,29 -25.1,14.5 -25.1,-14.5" fill="#46a8dc"/><path d="M-15 0 A15 13 0 0 1 15 0 Z" fill="#fff"/><rect x="-1" y="0" width="2" height="7" fill="#fff"/><circle cx="-7" cy="7" r="3" fill="#fff"/><circle cx="7" cy="7" r="3" fill="#fff"/><path d="M-12 15 a5 4 0 0 1 10 0 Z M2 15 a5 4 0 0 1 10 0 Z" fill="#fff"/></svg>
      <span class="service-label">Umbrella</span>
    </div>
    <div class="service" style="left:328px">
      <svg viewBox="-36 -36 72 72"><polygon points="0,-34 29.4,-17 29.4,17 0,34 -29.4,17 -29.4,-17" fill="#fff" stroke="#d81b60" stroke-width="2"/><polygon points="0,-29 25.1,-14.5 25.1,14.5 0,29 -25.1,14.5 -25.1,-14.5" fill="#46a8dc"/><path d="M0 6 C-12 -2 -10 -13 -4 -13 C-1 -13 0 -10 0 -9 C0 -10 1 -13 4 -13 C10 -13 12 -2 0 6Z" fill="#fff"/><path d="M-15 8 L-6 12 L8 12 L15 6" fill="none" stroke="#fff" stroke-width="3" stroke-linecap="round"/></svg>
      <span class="service-label">Life</span>
    </div>
    <div class="service" style="left:423px">
      <svg viewBox="-36 -36 72 72"><polygon points="0,-34 29.4,-17 29.4,17 0,34 -29.4,17 -29.4,-17" fill="#fff" stroke="#d81b60" stroke-width="2"/><polygon points="0,-29 25.1,-14.5 25.1,14.5 0,29 -25.1,14.5 -25.1,-14.5" fill="#46a8dc"/><rect x="-12" y="-14" width="12" height="27" fill="#fff"/><rect x="2" y="-5" width="10" height="18" fill="#fff"/><rect x="-15" y="13" width="30" height="2" fill="#fff"/><g fill="#46a8dc"><rect x="-9" y="-10" width="2" height="3"/><rect x="-5" y="-10" width="2" height="3"/><rect x="-9" y="-4" width="2" height="3"/><rect x="-5" y="-4" width="2" height="3"/><rect x="-9" y="2" width="2" height="3"/><rect x="-5" y="2" width="2" height="3"/><rect x="5" y="0" width="4" height="2"/><rect x="5" y="5" width="4" height="2"/></g></svg>
      <span class="service-label">Commercial</span>
    </div>
    <div class="service" style="left:518px">
      <svg viewBox="-36 -36 72 72"><polygon points="0,-34 29.4,-17 29.4,17 0,34 -29.4,17 -29.4,-17" fill="#fff" stroke="#d81b60" stroke-width="2"/><polygon points="0,-29 25.1,-14.5 25.1,14.5 0,29 -25.1,14.5 -25.1,-14.5" fill="#46a8dc"/><path d="M-15 5 L-15 -1 L-10 -2 L-6 -8 L7 -8 L11 -2 L15 -1 L15 5 Z" fill="#fff"/><circle cx="-8" cy="5" r="4" fill="#fff" stroke="#46a8dc" stroke-width="2"/><circle cx="8" cy="5" r="4" fill="#fff" stroke="#46a8dc" stroke-width="2"/></svg>
      <span class="service-label">Auto</span>
    </div>
    <div class="service" style="left:614px">
      <svg viewBox="-36 -36 72 72"><polygon points="0,-34 29.4,-17 29.4,17 0,34 -29.4,17 -29.4,-17" fill="#fff" stroke="#d81b60" stroke-width="2"/><polygon points="0,-29 25.1,-14.5 25.1,14.5 0,29 -25.1,14.5 -25.1,-14.5" fill="#46a8dc"/><path d="M-14 0 L0 -13 L14 0 L10 0 L10 12 L-10 12 L-10 0 Z" fill="#fff"/><circle cx="4" cy="6" r="7" fill="#46a8dc" stroke="#fff" stroke-width="2"/><text x="4" y="10" text-anchor="middle" font-family="Poppins, sans-serif" font-size="10" font-weight="700" fill="#fff">$</text></svg>
      <span class="service-label">Renters</span>
    </div>
    <div class="service" style="left:708px">
      <svg viewBox="-36 -36 72 72"><polygon points="0,-34 29.4,-17 29.4,17 0,34 -29.4,17 -29.4,-17" fill="#fff" stroke="#d81b60" stroke-width="2"/><polygon points="0,-29 25.1,-14.5 25.1,14.5 0,29 -25.1,14.5 -25.1,-14.5" fill="#46a8dc"/><path d="M0 4 C-11 -3 -9 -13 -4 -13 C-1 -13 0 -11 0 -10 C0 -11 1 -13 4 -13 C9 -13 11 -3 0 4Z" fill="#fff"/><path d="M-1 -8h2v2h2v2h-2v2h-2v-2h-2v-2h2z" fill="#46a8dc"/><path d="M-14 -4 L-12 8 L-3 14 M14 -4 L12 8 L3 14" fill="none" stroke="#fff" stroke-width="3" stroke-linecap="round"/></svg>
      <span class="service-label">Health</span>
    </div>
  </section>

  <footer class="contact-band">
    <div class="contact-item contact-address">
      <svg viewBox="0 0 24 24" fill="none" stroke="#fff" stroke-width="2.4"><path d="M12 22s-7-7-7-12a7 7 0 0 1 14 0c0 5-7 12-7 12z"/><circle cx="12" cy="10" r="2.5"/></svg>
      <span>27 Harbor Lane, Riverton, New York</span>
    </div>
    <div class="contact-item contact-email">
      <svg viewBox="0 0 24 24" fill="none" stroke="#fff" stroke-width="2.2"><rect x="3" y="6" width="18" height="12"/><path d="M3 6l9 7 9-7"/></svg>
      <span>hello@keystoneagency.com</span>
    </div>
  </footer>
</main>
</body>
</html>
```